Business Card Re-Design/Update

We'd like to update out business cards. I've included our current "Style guide" which has the colour scheme of the organisation in it. I've also included the branding files with logos etc in them.

I've also included a copy of one of our existing cards so that you can see how ugly/dated they look. I'd like a fresh modern corporate look.

Target Market(s)

These are for our clients, potential clients, industry contacts - like all business cards

Contact Information for Business Card

Name
Position
Company Address - Level 1, 47 Garnet Lane, Toowong Qld 4066
Direct Phone
mobile
Email
Website -www.korvalnet.com.au
Logo

Colors

Designer to choose colors to be used in the design.

Requirements
Must have
• Main Logo
• Cards will need to be editable to be able to personalize them for each new employee.
Nice to have
• The MapOUT, HandOVER, UpKEEP would be okay to have if they can be sensibly and professionally added to the look without detracting from the main imagery.
• Maybe they could go on the back of the card? will leave this to your creative discretion as to whether/where they fit.
Should not have
• Should not have decorative or script fonts

```html
<!DOCTYPE html>
<html lang="en">
<head>
<meta charset="utf-8">
<title>korvalnet business card</title>
<link href="https://fonts.googleapis.com/css2?family=Roboto+Condensed:wght@300;400;700&display=swap" rel="stylesheet">
<style>
  :root {
    --brand-red: #d71920;
    --charcoal: #3b3b3d;
    --ink: #1e1e1e;
    --text-grey: #6b6b6d;
    --light-grey: #8a8a8c;
    --paper: #ffffff;
    --card-bg-centre: #ffffff;
    --card-bg-edge: #e9e9ea;
  }
  html, body {
    margin: 0;
    width: 1200px;
    height: 1200px;
    overflow: hidden;
    background: var(--paper);
    font-family: "Roboto Condensed", "Arial Narrow", sans-serif;
  }
  .card {
    position: absolute;
    left: 398px;
    width: 403px;
    height: 230px;
    overflow: hidden;
  }
  .card--front {
    top: 333px;
    background: radial-gradient(ellipse at 45% 45%, var(--card-bg-centre) 0%, #f6f6f6 45%, var(--card-bg-edge) 100%);
  }
  .card--back {
    top: 637px;
    background: var(--brand-red);
  }
  .wordmark {
    position: absolute;
    left: 21px;
    display: flex;
    align-items: center;
    gap: 8px;
    font-weight: 400;
    font-size: 30px;
    letter-spacing: 0.2px;
    line-height: 1;
  }
  .wordmark__square {
    width: 18px;
    height: 18px;
    background: var(--brand-red);
  }
  .card--front .wordmark { top: 26px; color: var(--charcoal); }
  .card--back .wordmark { top: 20px; color: var(--paper); }
  .card--back .wordmark__square { background: var(--paper); }

  .person {
    position: absolute;
    right: 22px;
    top: 128px;
    text-align: right;
  }
  .person__name {
    font-size: 18px;
    font-weight: 400;
    color: var(--ink);
    line-height: 1;
  }
  .person__role {
    font-size: 10px;
    font-weight: 300;
    color: var(--light-grey);
    margin-top: 1px;
  }
  .contact {
    position: absolute;
    left: 21px;
    top: 148px;
    font-size: 8.4px;
    color: var(--light-grey);
    line-height: 13px;
  }
  .contact__address {
    font-size: 9.4px;
    font-weight: 700;
    color: var(--text-grey);
  }
  .contact__sep { padding: 0 8px; }
  .footer-band { position: absolute; left: 0; bottom: 0; }
  .web {
    position: absolute;
    font-size: 11.5px;
    font-weight: 300;
    color: var(--paper);
    letter-spacing: 0.3px;
  }
  .web strong { font-weight: 700; }
  .card--front .web { right: 23px; bottom: 10px; }
  .card--back .web { left: 21px; bottom: 18px; }
  .back-panel { position: absolute; left: 0; top: 0; }
</style>
</head>
<body>
  <section class="card card--front">
    <div class="wordmark"><span class="wordmark__square"></span>korvalnet</div>

    <div class="person">
      <div class="person__name">Maren Holt</div>
      <div class="person__role">Business Development Manager</div>
    </div>

    <div class="contact">
      <div class="contact__address">Level 1, 47 Garnet Lane, Toowong Qld 4066</div>
      <div>M &nbsp;+61 (0)412 555 018<span class="contact__sep">I</span>D &nbsp;+61 (0)7 3100 4416</div>
      <div>P &nbsp;&nbsp;+61 (0)7 3100 4400<span class="contact__sep">I</span>F &nbsp;+61 (0)7 3100 4401</div>
      <div>E &nbsp;mholt@korvalnet.com.au</div>
    </div>

    <svg class="footer-band" width="403" height="33" viewBox="0 0 403 33">
      <rect x="0" y="11" width="240" height="9" fill="var(--brand-red)"/>
      <path d="M0 20 H220 C238 20 236 0 258 0 H403 V33 H0 Z" fill="var(--charcoal)"/>
    </svg>
    <div class="web">www.<strong>korvalnet</strong>.com.au</div>
  </section>

  <section class="card card--back">
    <svg class="back-panel" width="403" height="230" viewBox="0 0 403 230">
      <polygon points="275,0 403,0 403,230 280,230" fill="var(--charcoal)"/>
    </svg>
    <div class="wordmark"><span class="wordmark__square"></span>korvalnet</div>
    <div class="web">www.<strong>korvalnet</strong>.com.au</div>
  </section>
</body>
</html>
```